Tindale Cosmetic Clinic

I would like a youthful fresh design that appeals to women 25-75 age bracket...Colours purples/pinks/splash orange something like:

Refresh, renew ,revitalize!

Book in for a consult! Only $80
An experienced, specialist cosmetic physician will give you a personalized insight into your treatment requirements using antiwrinkle injections and fillers
Your consultation fee will be refunded if you opt to go ahead with treatment.

www.tindalecosmetic-demo.com
located Within Tindale Medical Clinic, 7C pellam st, ferrow 5209
phone 0491 637584 and speak to Rhona

Drs Marguerite Volk ,Tarek Qudsi and Yvonne Pettigrew

```html
<!DOCTYPE html>
<html lang="en">
<head>
<meta charset="utf-8">
<title>Tindale Cosmetic Clinic</title>
<link rel="stylesheet" href="https://fonts.googleapis.com/css2?family=Questrial&family=Lobster&family=Roboto+Condensed:wght@700&display=swap">
<style>
  :root {
    --lavender: #aaa4cf;
    --lavender-deep: #8f87bf;
    --ink: #1c1c1e;
    --mist: #eeeeef;
    --grey-strip: #d2d3d5;
    --white: #ffffff;
  }
  html, body {
    margin: 0;
    width: 910px;
    height: 1200px;
    overflow: hidden;
    background: var(--white);
  }
  .flyer {
    position: absolute;
    left: 94px;
    top: 171px;
    width: 650px;
    height: 838px;
    transform: rotate(-90deg);
    transform-origin: center;
    overflow: hidden;
    background: linear-gradient(90deg, #f7f7f8 0%, var(--mist) 45%, #d9d9db 100%);
    font-family: "Questrial", "Century Gothic", sans-serif;
    color: var(--ink);
  }
  .edge-strip {
    position: absolute; left: 0; top: 0; width: 100%; height: 38px;
    background: linear-gradient(180deg, #e4e5e6, var(--grey-strip));
  }
  .tagline-band {
    position: absolute; left: 0; top: 38px; width: 100%; height: 66px;
    background: var(--lavender);
    border-bottom: 3px solid var(--white);
    box-sizing: border-box;
  }
  .tagline {
    position: absolute; left: 34px; top: 8px; margin: 0;
    font-size: 40px; font-weight: 400; letter-spacing: 2.5px;
    color: var(--white); white-space: nowrap;
  }
  .portrait {
    position: absolute; left: 250px; top: 104px; width: 400px; height: 660px;
    background: linear-gradient(90deg, rgba(238,238,239,0) 0%, #d6d6d8 35%, #bdbdc0 70%, #9a9a9d 100%);
  }
  .clinic-name {
    position: absolute; left: 14px; top: 108px; margin: 0;
    font-family: "Lobster", cursive; font-weight: 400;
    font-size: 66px; color: var(--lavender-deep); white-space: nowrap;
  }
  .treatments { position: absolute; left: 40px; top: 244px; }
  .treatments-title { margin: 0 0 6px; font-size: 20px; font-weight: 400; }
  .treatments ul { list-style: none; margin: 0; padding: 0; }
  .treatments li { font-size: 22px; line-height: 27px; }
  .treatments li::before { content: "•"; color: var(--lavender); margin-right: 8px; }
  .doctors { position: absolute; left: 40px; top: 425px; margin: 0; padding: 0; list-style: none; }
  .doctors li { font-size: 19px; line-height: 30px; }
  .offer { position: absolute; left: 36px; top: 548px; display: flex; align-items: center; }
  .price {
    font-family: "Roboto Condensed", "Arial Narrow", sans-serif; font-weight: 700;
    font-size: 52px; line-height: 1; letter-spacing: -1px;
  }
  .offer-note { margin-left: 10px; font-size: 19px; line-height: 18px; color: var(--lavender-deep); }
  .phone { position: absolute; left: 36px; top: 626px; display: flex; align-items: center; }
  .phone svg { width: 24px; height: 30px; margin-right: 6px; }
  .phone-number {
    font-family: "Roboto Condensed", "Arial Narrow", sans-serif; font-weight: 700;
    font-size: 36px; line-height: 1;
  }
  .contact-person { position: absolute; left: 78px; top: 672px; font-size: 19px; color: var(--lavender-deep); }
  .footer-wave { position: absolute; left: 0; top: 0; width: 650px; height: 838px; }
  .location { position: absolute; left: 62px; top: 766px; font-size: 17px; line-height: 27px; }
  .location .address { font-size: 15px; }
  .website {
    position: absolute; left: 372px; top: 790px;
    font-family: "Questrial", sans-serif; font-weight: 400;
    font-size: 19px; letter-spacing: 0.3px; color: var(--ink);
  }
</style>
</head>
<body>
  <div class="flyer">
    <div class="edge-strip"></div>
    <div class="tagline-band"><h2 class="tagline">Refresh, Renew, Revitalize!</h2></div>

    <div class="portrait" role="img" aria-label="Soft black and white photo of a woman resting her cheek on her hand, eyes closed"></div>

    <svg class="footer-wave" viewBox="0 0 650 838" aria-hidden="true">
      <path d="M0,820 C60,812 90,790 150,792 C260,796 330,780 400,745 C480,705 540,640 650,625 L650,838 L0,838 Z" fill="var(--lavender)"/>
    </svg>

    <h1 class="clinic-name">Tindale Cosmetic Clinic</h1>

    <section class="treatments">
      <h3 class="treatments-title">Treatments:</h3>
      <ul>
        <li>Antiwrinkle Injections</li>
        <li>Facial Fillers</li>
        <li>Lip Enhancement</li>
        <li>Volume Restoration</li>
      </ul>
    </section>

    <ul class="doctors">
      <li>Dr. Marguerite Volk</li>
      <li>Dr. Yvonne Pettigrew</li>
      <li>Dr. Tarek Qudsi</li>
    </ul>

    <div class="offer">
      <span class="price">$80</span>
      <span class="offer-note">Book in for<br>a consult!</span>
    </div>

    <div class="phone">
      <svg viewBox="0 0 24 30" aria-hidden="true">
        <path d="M8,2 C3,6 2,14 4,20 C6,25 10,28 14,28 L16,23 L12,21 C10,19 9,14 10,10 L14,9 L13,3 Z" fill="var(--ink)"/>
      </svg>
      <span class="phone-number">0491 637 584</span>
    </div>
    <div class="contact-person">(speak to Rhona)</div>

    <div class="location">
      Within Tindale Medical Clinic<br>
      <span class="address">7c Pellam Street, Ferrow 5209</span>
    </div>
    <div class="website">www.tindalecosmetic-demo.com</div>
  </div>
</body>
</html>
```